Kestrel Nine (IT/Network Services)

Kestrel Nine, LLC provides technology services to small and medium businesses. Essentially, anytime you've every thought your business might need an "IT guy" to handle something you could instead call us to handle it. Basically, you can outsource your IT needs to us.

This is a brand new company and so we'll need a brand new website. I'd like to use WordPress to handle the site since that will make things easier for me to maintain in the long run.

The site should include a, more-or-less, static front page with the dynamic data occurring on pages linked from a navigational area.

I have a logo already designed that I would like to see used in the design. The one with "white" in the title is the official logo, just added some other versions for your perusal.

Color queues from the logo but feel free to add other colors where applicable.

The site should feel somewhat corporate but with a "younger" slant (something a 25-35 year old would enjoy).

Pages (either to be added initially or by me after design completion):
"About" section - includes company history, business philosophy, etc.
"Services" section - service options, service approach, service specifics
"Testimonials" section - (eventually)
"News" section - (eventually) industry news, company news, events, blog
Contact Links

Websites to view:
The two largest local competitors:
http://www.brimfieldsystemsco.com/
http://www.qmworkset.com/
Other local competitors:
http://www.pvrllc.com/
http://www.lorvanassociates.com/

Other info you might find useful:
Domain: knllc.com
Address:
517 Hollis Row E
Suite 812B
Nashville, TN 37219
Phone: 615-382-7140
Emails available for use/display:
info@knllc.com
sales@knllc.com

Target Market(s)

Our target clients are mainly small businesses (25 or less computer users) which means we're looking at a lot of start-ups or younger companies. We'll be interacting with many entrepreneurs and young business owners.

Requirements
Must have
• Need full WP theme (not a mockup)

```html
<!DOCTYPE html>
<html lang="en">
<head>
<meta charset="utf-8">
<title>Kestrel Nine – IT &amp; Network Services</title>
<link href="https://fonts.googleapis.com/css2?family=Ubuntu:wght@400;500;700&family=PT+Sans:wght@400;700&display=swap" rel="stylesheet">
<style>
:root{
  --orange:#f08a1c;
  --orange-dark:#d9700a;
  --orange-light:#f6a445;
  --charcoal:#3a3a3a;
  --nav-dark:#2b2b2b;
  --text:#444;
  --muted:#666;
  --panel:#f1f1f1;
  --line:#dcdcdc;
  --white:#fff;
  --footer:#4a4a4a;
}
*{box-sizing:border-box;margin:0;padding:0}
html,body{width:1023px;height:1200px;overflow:hidden}
body{position:relative;background:var(--white);font-family:"PT Sans",Arial,sans-serif;color:var(--text)}
.abs{position:absolute}
.heading-font{font-family:"Ubuntu",Arial,sans-serif}

/* header */
.site-header{left:0;top:0;width:1023px;height:149px;background:linear-gradient(#fff 0%,#fff 40%,#e6e6e6 100%);border-top:3px solid #666}
.brand{left:90px;top:62px;display:flex;align-items:center;gap:10px}
.brand-mark{width:30px;height:30px;border-radius:50%;background:var(--orange)}
.brand-name{font-family:"Ubuntu",Arial,sans-serif;font-weight:500;font-size:30px;color:#6b6b6b;letter-spacing:.5px}
.call-box{left:699px;top:0;width:224px;height:43px;background:linear-gradient(#4a4a4a,#1f1f1f);border-radius:0 0 8px 8px;display:flex;align-items:center;padding-left:14px;gap:10px}
.call-box .label{font-family:"Ubuntu",Arial,sans-serif;font-weight:700;font-size:17px;color:var(--orange)}
.call-box .label span{color:#fff}
.follow{left:747px;top:99px;display:flex;align-items:center;gap:4px;font-family:"Ubuntu",Arial,sans-serif;font-weight:500;font-size:13px;color:#555}
.follow .dot{width:20px;height:20px;border-radius:50%;background:#3b6db3;margin-left:2px}
.follow .dot.alt{background:#f2872a}
.follow .dot.sky{background:#42a9dc}

/* nav */
.main-nav{left:105px;top:130px;width:824px;height:41px;background:linear-gradient(#555,#1e1e1e);border-radius:10px;border:2px solid #fff;box-shadow:0 0 0 1px #bbb;z-index:2}
.main-nav ul{list-style:none;position:relative;height:100%}
.main-nav li{position:absolute;top:0;height:100%;display:flex;align-items:center;justify-content:center;font-family:"Ubuntu",Arial,sans-serif;font-size:12px;color:#fff;border-right:1px solid #111;box-shadow:1px 0 0 #666}
.main-nav li.active{background:linear-gradient(var(--orange-light),var(--orange-dark))}

/* hero */
.hero{left:0;top:149px;width:1023px;height:333px;background:repeating-linear-gradient(90deg,#f29a33 0,#ee8a1f 3px,#f39d3a 6px);}
.hero-divider{left:0;top:482px;width:1023px;height:6px;background:#e3e3e3}
.hero-title{left:111px;top:194px;font-family:"Ubuntu",Arial,sans-serif;font-weight:700;font-size:20px;line-height:27px;color:#fff}
.hero-title b{color:#2d2d2d}
.hero-lead{left:111px;top:257px;width:380px;font-family:"Ubuntu",Arial,sans-serif;font-weight:500;font-size:14px;line-height:15.5px;color:#fff}
.hero-points{left:114px;top:320px;width:410px;list-style:none;font-size:11px;line-height:13.5px;color:#fff}
.hero-points li{position:relative;padding-left:18px;margin-bottom:7px}
.hero-points svg{position:absolute;left:0;top:1px}
.btn-services{left:118px;top:427px;width:135px;height:32px;background:linear-gradient(#fff,#e8e8e8);border-radius:16px;display:flex;align-items:center;padding-left:12px;gap:6px;font-family:"Ubuntu",Arial,sans-serif;font-weight:500;font-size:15px;color:#444;box-shadow:0 3px 4px rgba(0,0,0,.2)}
.btn-services b{color:var(--orange);font-weight:500}
.btn-services .ico{width:20px;height:20px;border-radius:50%;background:#ccc}
.hero-devices{left:569px;top:190px;width:353px;height:283px;border-radius:4px;background:linear-gradient(135deg,#f5f5f5,#d8d8d8 60%,#2d2d2d 61%,#444)}

/* cards */
.card{width:177px;height:212px;top:500px;background:linear-gradient(#fff,#ececec);border:1px solid var(--line);border-radius:6px}
.card-head{position:absolute;left:5px;top:5px;width:166px;height:28px;background:linear-gradient(var(--orange-light),var(--orange-dark));border-radius:6px;display:flex;align-items:center;justify-content:space-between;padding:0 10px 0 16px;font-family:"Ubuntu",Arial,sans-serif;font-weight:500;font-size:15px;color:#fff}
.card-head i{width:14px;height:14px;border:2px solid #fff;border-radius:50%}
.card-photo{position:absolute;left:8px;top:40px;width:159px;height:92px;background:linear-gradient(#f3e6d2,#c8a27a)}
.card p{position:absolute;left:9px;top:138px;width:158px;font-size:10px;line-height:15px;text-align:justify;color:#555}
.card .more{position:absolute;right:10px;top:192px;font-weight:700;font-size:10.5px;color:#444}

/* sidebar */
.booking{left:692px;top:511px;width:233px;height:104px;background:linear-gradient(var(--orange-light),var(--orange-dark));border-radius:6px}
.booking h3{position:absolute;left:15px;top:4px;font-family:"Ubuntu",Arial,sans-serif;font-weight:500;font-size:19px;color:#fff}
.booking h3 b{color:#2d2d2d;font-weight:500}
.booking .mini-brand{position:absolute;left:15px;top:76px;font-family:"Ubuntu",Arial,sans-serif;font-weight:500;font-size:13px;color:#fff;opacity:.85}
.booking .mini-mark{position:absolute;left:30px;top:34px;width:32px;height:32px;border:3px solid #fde7cc;border-radius:50%}
.btn-dark{position:absolute;left:146px;top:67px;width:74px;height:28px;background:linear-gradient(#555,#1e1e1e);border:2px solid #fff;border-radius:7px;color:#fff;font-family:"Ubuntu",Arial,sans-serif;font-size:12px;display:flex;align-items:center;justify-content:center}
.quote{left:692px;top:639px;width:233px;height:190px;background:linear-gradient(#fff,#e6e6e6);border:1px solid var(--line);border-radius:10px}
.quote blockquote{position:absolute;left:19px;top:24px;width:200px;font-family:"Ubuntu",Arial,sans-serif;font-size:10.5px;line-height:20.5px;color:#555}
.quote .qmark{position:absolute;font-family:Georgia,serif;font-size:22px;color:#555}
.quote cite{position:absolute;right:17px;top:138px;text-align:right;font-style:normal;font-size:9.5px;line-height:13.7px;color:#444}
.callback{left:692px;top:852px;width:233px;height:163px;background:linear-gradient(#fff,#e2e2e2);border:1px solid var(--line);border-radius:10px}
.callback h3{position:absolute;left:43px;top:9px;font-family:"Ubuntu",Arial,sans-serif;font-weight:500;font-size:19px;color:#444}
.callback .ico{position:absolute;left:10px;top:10px}
.field{position:absolute;left:11px;width:210px;height:22px;background:linear-gradient(#f0f0f0,#fff);border:1px solid #d5d5d5;border-radius:11px;padding-left:13px;font-size:10.5px;line-height:20px;color:#777}
.btn-send{position:absolute;left:142px;top:121px;width:77px;height:25px;background:linear-gradient(#42a9e8,#1a74c4);border:2px solid #fff;border-radius:7px;box-shadow:0 0 0 1px #bbb;color:#fff;font-family:"Ubuntu",Arial,sans-serif;font-weight:500;font-size:12px;display:flex;align-items:center;justify-content:center}
.callback .figure{position:absolute;left:20px;top:112px;width:100px;height:38px;border-radius:4px;background:linear-gradient(90deg,#f7c56a,#e2e2e2)}

/* about */
.about{left:96px;top:750px;width:560px}
.about h2{font-family:"Ubuntu",Arial,sans-serif;font-weight:500;font-size:20px;color:#444}
.about h2 span{color:var(--orange)}
.about .intro{margin-top:8px;font-weight:700;font-size:10px;line-height:17px;color:#333}
.about h4{margin-top:8px;font-weight:700;font-size:11px;color:#e0901a}
.about ul{list-style:none;margin-top:10px;font-size:10px;line-height:17px;color:#444}
.about li{position:relative;padding-left:31px}
.about li::before{content:"";position:absolute;left:18px;top:6px;border-left:4px solid var(--orange);border-top:3px solid transparent;border-bottom:3px solid transparent}
.about .cta{margin-top:15px;font-weight:700;font-size:11.5px;color:#444}

/* footer */
.site-footer{left:0;top:1067px;width:1023px;height:133px;background:linear-gradient(#555,#3b3b3b);border-top:3px dotted #777}
.foot-links{left:104px;top:1101px;font-size:10.5px;color:#ccc;letter-spacing:.4px;word-spacing:2px}
.foot-links span{margin:0 10px}
.foot-copy{left:104px;top:1122px;font-size:10.5px;color:#ccc;letter-spacing:.3px}
.foot-follow{left:105px;top:1149px;display:flex;align-items:center;gap:3px;font-size:10.5px;color:#ccc}
.foot-follow i{width:16px;height:16px;background:#ddd;border-radius:2px;margin-left:3px}
.foot-contact{right:93px;top:1073px;text-align:right;font-size:9.5px;line-height:15.3px;color:#fff}
.foot-contact h3{font-family:"Ubuntu",Arial,sans-serif;font-weight:500;font-size:15px;margin-bottom:3px;margin-right:-6px}
</style>
</head>
<body>

<header class="abs site-header"></header>
<div class="abs brand"><span class="brand-mark"></span><span class="brand-name">Kestrel Nine</span></div>
<div class="abs call-box">
  <svg width="20" height="20" viewBox="0 0 24 24"><path d="M6.6 10.8a15 15 0 0 0 6.6 6.6l2.2-2.2c.3-.3.7-.4 1-.2 1.1.4 2.3.6 3.6.6.6 0 1 .4 1 1V20c0 .6-.4 1-1 1A17 17 0 0 1 3 4c0-.6.4-1 1-1h3.5c.6 0 1 .4 1 1 0 1.3.2 2.5.6 3.6.1.3 0 .7-.2 1z" fill="#f08a1c"/></svg>
  <span class="label">CALL : <span>615-382-7140</span></span>
</div>
<div class="abs follow">Follow us : <i class="dot"></i><i class="dot"></i><i class="dot alt"></i><i class="dot sky"></i></div>

<nav class="abs main-nav">
  <ul>
    <li class="active" style="left:12px;width:72px">HOME</li>
    <li style="left:104px;width:106px">ABOUT US</li>
    <li style="left:210px;width:111px">SERVICES</li>
    <li style="left:321px;width:131px">TESTIMONIAL</li>
    <li style="left:452px;width:112px">CONTACT US</li>
  </ul>
</nav>

<section class="abs hero"></section>
<div class="abs hero-divider"></div>
<h1 class="abs hero-title">COMPREHENSIVE COMPUTER NETWORK<br>SUPPORT FOR YOUR <b>BUSINESS</b></h1>
<p class="abs hero-lead">Northgate Network Group provides comprehensive computer network support to businesses that are ready to stop trying to fix technology</p>
<ul class="abs hero-points">
  <li><svg width="12" height="11" viewBox="0 0 12 11"><path d="M1 6l3 4 7-9" stroke="#3a2a10" stroke-width="2.2" fill="none"/></svg>Enjoy greater productivity because they have less downtime</li>
  <li><svg width="12" height="11" viewBox="0 0 12 11"><path d="M1 6l3 4 7-9" stroke="#3a2a10" stroke-width="2.2" fill="none"/></svg>Focus on the growth of their business rather than shoulder the burdens of managing their IT</li>
  <li><svg width="12" height="11" viewBox="0 0 12 11"><path d="M1 6l3 4 7-9" stroke="#3a2a10" stroke-width="2.2" fill="none"/></svg>Capitalize on opportunities to enrich their business through technology</li>
  <li><svg width="12" height="11" viewBox="0 0 12 11"><path d="M1 6l3 4 7-9" stroke="#3a2a10" stroke-width="2.2" fill="none"/></svg>Confidently know their data and their network is secure</li>
</ul>
<div class="abs btn-services"><span class="ico"></span>Our <b>Services</b></div>
<div class="abs hero-devices" role="img" aria-label="Website shown on a desktop browser, tablet and phone"></div>

<article class="abs card" style="left:97px">
  <div class="card-head">About us<i></i></div>
  <div class="card-photo" role="img" aria-label="Team members carrying moving boxes"></div>
  <p>Lorem Ipsum is simply dummy text of the printing and typesetting industry.</p>
  <span class="more">Moreinfo[+]</span>
</article>
<article class="abs card" style="left:294px">
  <div class="card-head">Services<i></i></div>
  <div class="card-photo" role="img" aria-label="Couple unpacking among cardboard boxes"></div>
  <p>Lorem Ipsum is simply dummy text of the printing and typesetting industry.</p>
  <span class="more">Moreinfo[+]</span>
</article>
<article class="abs card" style="left:492px">
  <div class="card-head">Testimonial<i></i></div>
  <div class="card-photo" role="img" aria-label="Happy clients standing beside stacked boxes"></div>
  <p>Lorem Ipsum is simply dummy text of the printing and typesetting industry.</p>
  <span class="more">Moreinfo[+]</span>
</article>

<aside class="abs booking">
  <h3>Get <b>Online</b> Booking</h3>
  <span class="mini-mark"></span>
  <span class="mini-brand">Kestrel Nine</span>
  <span class="btn-dark">Book Now</span>
</aside>

<aside class="abs quote">
  <span class="qmark" style="left:6px;top:10px">“</span>
  <blockquote>Marcus and his staff have proven time and again that they have the experience, knowledge and confidence to respond to whatever challenge we can throw in their path.</blockquote>
  <span class="qmark" style="left:145px;top:111px">”</span>
  <cite>Daniel Whitcombe<br>Chief Financial Officer<br>Harbor Ridge Medical Group</cite>
</aside>

<aside class="abs callback">
  <svg class="ico" width="28" height="28" viewBox="0 0 24 24"><path d="M6.6 10.8a15 15 0 0 0 6.6 6.6l2.2-2.2c.3-.3.7-.4 1-.2 1.1.4 2.3.6 3.6.6.6 0 1 .4 1 1V20c0 .6-.4 1-1 1A17 17 0 0 1 3 4c0-.6.4-1 1-1h3.5c.6 0 1 .4 1 1 0 1.3.2 2.5.6 3.6.1.3 0 .7-.2 1z" fill="#888"/></svg>
  <h3>Get a call back</h3>
  <div class="field" style="top:46px">Your Name :</div>
  <div class="field" style="top:80px">Your Phone No :</div>
  <div class="figure" role="img" aria-label="Figure relaxing with a laptop"></div>
  <span class="btn-send">Send Now</span>
</aside>

<section class="abs about">
  <h2><span>About</span> Kestrel Nine Services</h2>
  <p class="intro">We are accredited by Regional Office Movers Guild. ROMG is the governing organisation and sets the standard for Regional Office Movers.</p>
  <h4>Businesses who have partnered with NNG:</h4>
  <ul>
    <li>Enjoy greater productivity because they have less downtime</li>
    <li>Focus on the growth of their business rather than shoulder the burdens of managing their IT</li>
    <li>Capitalize on opportunities to enrich their business through technology</li>
    <li>Confidently know their data and their network is secure</li>
    <li>Enjoy greater productivity because they have less downtime</li>
    <li>Focus on the growth of their business rather than shoulder the burdens of managing their IT</li>
    <li>Capitalize on opportunities to enrich their business through technology</li>
    <li>Confidently know their data and their network is secure</li>
  </ul>
  <p class="cta">What are you waiting for? Call us NOW on 02 5550 1834. We will exceed your expectations.</p>
</section>

<footer class="abs site-footer"></footer>
<div class="abs foot-links">Home<span>|</span>About us<span>|</span>Services<span>|</span>Testimonial<span>|</span>Contact us</div>
<div class="abs foot-copy">Kestrel Nine Pvt. Ltd. © 2011-12 Copy Rights &nbsp; Terms and Conditions &nbsp;| Privacy Policy</div>
<div class="abs foot-follow">Follow us on : <i></i><i></i><i></i><i></i><i></i></div>
<address class="abs foot-contact" style="font-style:normal">
  <h3>Contact us @</h3>
  517 Hollis Row E Suite 812B<br>
  Nashville, TN 37219<br>
  Phone: 615-382-7140<br>
  Emails available for use/display:<br>
  info@knllc.com<br>
  sales@knllc.com
</address>

</body>
</html>
```